Pizza Box 10" x 10" - color: White

Custom design, utilizing CrustLoomo Logo and include the following information on the Pizza Box:

1. Custom Crafted Pizza with Quality Ingredients.
2. [....Get Your GAME ON] to be placed on the front flap and seen when the
box is opened.
3. You"ll miss 100% of the Pizza you don't eat.

4. Visit www.fennelcartonworks.example for additional design resource information. Go to site and then click on ORDERING to access.

5. The 10" x 10" Pizza Box is to be in the color WHITE.
6. Use colors Black and Red. no generic images. no food pics. I am looking for a clean and cool design.

Target Market(s)

Age 16 - 36 years

Industry/Entity Type

American Restaurant

Font styles to use
Sans Serif

Colors
ec1f27
000000
ffffff

Requirements
Must have
• Color Red and Black.
• Logo on Top and all sides of the Pizza Box.
Nice to have
• A Creative design that does not look generic.
Should not have
• No food images.

```html
<!DOCTYPE html>
<html lang="en">
<head>
<meta charset="utf-8">
<title>CrustLoomo 10" Pizza Box</title>
<link rel="stylesheet" href="https://fonts.googleapis.com/css2?family=Bebas+Neue&family=Josefin+Sans:wght@300&display=swap">
<style>
  :root {
    --brand-red: #ec1f27;
    --brand-ink: #333333;
    --board-white: #ffffff;
    --lid-white: #f5f5f5;
    --cut-line: #444444;
    --frame-line: #cccccc;
  }
  html, body { margin: 0; padding: 0; overflow: hidden; background: var(--board-white); }
  .canvas { width: 1200px; height: 1018px; display: block; }
  .frame { fill: var(--board-white); stroke: var(--frame-line); stroke-width: 1.5; }
  .cut { fill: none; stroke: var(--cut-line); stroke-width: 1.3; stroke-linejoin: round; }
  .fold { fill: none; stroke: var(--cut-line); stroke-width: 1.1; stroke-dasharray: 6 5; }
  .print-band { fill: none; stroke: var(--brand-red); stroke-width: 1.2; }
  .display { font-family: "Bebas Neue", "Oswald", sans-serif; }
  .ink { fill: var(--brand-ink); }
  .red { fill: var(--brand-red); }
  .subline { font-family: "Josefin Sans", "Helvetica", sans-serif; font-weight: 300; fill: var(--brand-ink); letter-spacing: 0.06em; }
  .brand-mark { fill: none; stroke: var(--brand-red); }
  .lid-face { fill: var(--lid-white); stroke: #bbbbbb; stroke-width: 1.5; }
  .lid-edge { fill: #eeeeee; stroke: #bbbbbb; stroke-width: 1.2; }
  .size-mark { font-family: "Bebas Neue", sans-serif; fill: #222; }
</style>
</head>
<body>
<svg class="canvas" viewBox="0 0 1450 1230" xmlns="http://www.w3.org/2000/svg">
  <defs>
    <g id="slogan">
      <text class="display ink" x="-34" y="-4" font-size="8">YOU'LL MISS</text>
      <text class="display red" x="-34" y="10" font-size="15">100%</text>
      <text class="display ink" x="-3" y="2" font-size="5">OF THE</text>
      <text class="display red" x="6" y="0" font-size="14">PIZZA</text>
      <text class="display ink" x="6" y="9" font-size="8">YOU DON'T EAT.</text>
    </g>
  </defs>

  <rect class="frame" x="1" y="1" width="1448" height="1228"/>

  <!-- Dieline -->
  <g class="dieline">
    <!-- top tuck flap and lid ears -->
    <path class="cut" d="M92 75 V218 M92 75 H148 V140 Q150 148 155 148 Q160 148 160 140 V75 H203 L210 68 H258 L265 75 H395 L402 68 H450 L457 75 H497 V140 Q497 148 502 148 Q508 148 508 140 V75 H565 V218"/>
    <path class="cut" d="M155 148 V218 M502 148 V218"/>
    <path class="fold" d="M160 140 H497"/>
    <path class="fold" d="M160 148 H497"/>
    <circle class="cut" cx="328" cy="143" r="17" fill="#fff"/>
    <path class="cut" d="M155 210 H200 V222 H260 L265 210 H392 V222 H455 V210 H502"/>
    <path class="cut" d="M92 218 H155 M502 218 H565"/>

    <!-- lid and its side flaps -->
    <path class="cut" d="M92 218 V565 M565 218 V565"/>
    <path class="fold" d="M155 218 V565 M502 218 V565"/>
    <path class="cut" d="M92 565 H155 M502 565 H565 M155 565 H502"/>

    <!-- lid front flap -->
    <path class="cut" d="M155 565 V625 L200 632 L212 625 H278 L288 632 H370 L380 625 H445 L457 632 L497 625 V565"/>
    <path class="cut" d="M92 565 V652 L160 632 M565 565 V652 L497 632"/>
    <text class="size-mark" x="537" y="618" font-size="30" text-anchor="middle">10</text>

    <!-- base with side walls -->
    <path class="fold" d="M160 632 V972 M497 632 V972"/>
    <path class="cut" d="M92 652 V740 L106 750 V862 L92 872 V940 L125 972 H160 M565 652 V740 L552 750 V862 L565 872 V940 L525 972 H497"/>
    <path class="cut" d="M160 825 H152 V905 H160 M497 825 H505 V905 H497"/>
    <path class="fold" d="M160 972 H310 M346 972 H497"/>
    <path class="cut" d="M310 972 Q328 1000 346 972"/>

    <!-- front wall -->
    <path class="cut" d="M160 972 V1000 L190 1040 H268 L275 1033 H380 L387 1040 H465 L497 1000 V972"/>

    <!-- print bands -->
    <rect class="print-band" x="177" y="170" width="302" height="33"/>
    <use href="#slogan" transform="translate(330 186)"/>
    <rect class="print-band" x="108" y="240" width="32" height="301"/>
    <use href="#slogan" transform="translate(124 381) rotate(90)"/>
    <rect class="print-band" x="515" y="240" width="33" height="301"/>
    <use href="#slogan" transform="translate(531 381) rotate(-90)"/>
    <rect class="print-band" x="177" y="580" width="302" height="33"/>
    <use href="#slogan" transform="translate(330 596) rotate(180)"/>
    <rect class="print-band" x="118" y="652" width="25" height="301"/>
    <use href="#slogan" transform="translate(130 800) rotate(90)"/>
    <rect class="print-band" x="513" y="652" width="26" height="301"/>
    <use href="#slogan" transform="translate(526 800) rotate(-90)"/>
    <rect class="print-band" x="177" y="993" width="302" height="27"/>
    <use href="#slogan" transform="translate(330 1006)"/>

    <!-- base artwork -->
    <rect class="print-band" x="177" y="652" width="302" height="301"/>
    <circle class="brand-mark" cx="253" cy="779" r="19" stroke-width="3.5"/>
    <text class="display ink" x="282" y="792" font-size="38">CrustLoomo</text>
    <text class="subline" x="342" y="819" font-size="5" text-anchor="middle">Custom Crafted Pizza with Quality Ingredients</text>
    <text class="display red" x="336" y="946" font-size="25" text-anchor="middle">GET YOUR GAME ON...</text>
  </g>

  <!-- Lid artwork, flat -->
  <g class="lid">
    <rect class="lid-face" x="620" y="168" width="718" height="704"/>
    <rect class="lid-edge" x="620" y="872" width="718" height="24"/>
    <circle cx="977" cy="870" r="47" fill="#fff" stroke="#bbbbbb" stroke-width="1.2"/>
    <circle class="brand-mark" cx="806" cy="434" r="51" stroke-width="7"/>
    <text class="display ink" x="880" y="462" font-size="92">CrustLoomo</text>
    <text class="subline" x="995" y="535" font-size="12" text-anchor="middle">Custom Crafted Pizza with Quality Ingredients</text>
    <text class="display red" x="1005" y="802" font-size="66" text-anchor="middle" letter-spacing="1">GET YOUR GAME ON...</text>
  </g>
</svg>
</body>
</html>
```